4.25" x 11" Door Hanger Design - Glass Bolt Internet Service

We are sourcing a door hanger that will be used to micro target specific neighborhoods with our new "Glass Bolt" internet service offering

This will be used as a template for a new type of plan we are offering in very specific areas. The first will be "Cedar Hollow" with 3 plan offerings.

Stock photos should be family friendly but we want something modern and exciting that we can use to advertise a new internet service offering.
Updates

Sorry if I missed this before, but we would of course like our website and phone number with an encouragement to call us Website: www.brivanet.example Phone: 555-304-2968

Target Market(s)

Residential Internet Service

Industry/Entity Type

Internet Service Provider

Font styles to use
Sans Serif
Other font styles liked:
• RockoFLF

Colors

Designer to choose colors to be used in the design.

Requirements
Must have
• 1) Our logo with "Internet Services" nearby to show "Brivanet Internet Services" (name and what we do)
• 2) "Glass Bolt Internet Service is Now Available in Cedar Hollow!"
• 3) Show three plans, we don't know the price yet and we will edit the winning design eventually when we know the exact price.
• 100 Mbps $XX.XX per month
• 250 Mbps $XX.XX per month
• 1 Gbps $XX.XX per month
• 4) The plan names and prices should be easy to edit in the future if/when we try these in different markets.
• This ad will be modified with specific information like prices and the location when we use it in specific spots.
• We will be using Printwagon for the printing, please use their website for the punch hole location, dimensions, etc.
• https://www.printwagon.example/door-hanger-printing/
Nice to have
• We want to demonstrate far higher than normal internet service speed offerings. This can use whatever you think demonstrates this idea to the customers better, something like a speed test looking logo
Should not have
• Do not copy our website, we want a fresh design

```html
<!DOCTYPE html>
<html lang="en">
<head>
<meta charset="utf-8">
<title>Brivanet Internet Services – Door Hanger</title>
<link rel="stylesheet" href="https://fonts.googleapis.com/css2?family=Open+Sans:wght@400;600&display=swap">
<style>
  :root {
    --charcoal: #2e2e30;
    --ink: #141416;
    --brand-blue: #3b8fd8;
    --plan-blue: #1e7fc8;
    --sky: #8fc5ec;
    --white: #ffffff;
    --mist-light: #cfd1d3;
    --mist-dark: #8e9093;
    --deep-navy: #0c2236;
    --ocean: #2f6c96;
  }
  * { box-sizing: border-box; margin: 0; padding: 0; }
  html, body { width: 1200px; height: 3327px; overflow: hidden; background: var(--white); }
  body { font-family: "Open Sans", Arial, sans-serif; }
  .hanger { position: relative; width: 1200px; height: 3327px; overflow: hidden; background: var(--mist-light); }

  .masthead { position: absolute; left: 0; top: 0; width: 1200px; height: 754px; background: var(--charcoal); }
  .punch-hole { position: absolute; left: 490px; top: 50px; width: 220px; height: 220px; border-radius: 50%; background: var(--white); border: 4px solid var(--sky); }
  .brand { position: absolute; left: 0; top: 310px; width: 1200px; display: flex; justify-content: center; align-items: center; gap: 40px; }
  .brand-dot { width: 110px; height: 110px; border-radius: 50%; background: var(--brand-blue); }
  .brand-name { font-size: 190px; font-weight: 400; color: var(--brand-blue); line-height: 1; letter-spacing: -2px; }
  .brand-tagline { position: absolute; left: 0; top: 545px; width: 1200px; text-align: center; color: var(--white); font-size: 80px; font-weight: 400; line-height: 1.2; }

  .title-band { position: absolute; left: 0; top: 754px; width: 1200px; height: 155px; background: var(--sky); border-bottom: 22px solid var(--charcoal); display: flex; align-items: center; justify-content: center; }
  .title-band h1 { font-size: 76px; font-weight: 400; color: var(--charcoal); }

  .backdrop { position: absolute; left: 0; top: 931px; width: 1200px; height: 1500px; background: radial-gradient(ellipse at 60% 40%, var(--mist-light), var(--mist-dark)); }

  .plan { position: absolute; left: 140px; width: 1029px; height: 326px; background: var(--plan-blue); border: 11px solid var(--white); }
  .plan p { position: absolute; left: 177px; top: 42px; color: var(--white); font-size: 76px; line-height: 122px; }
  .plan-marker { position: absolute; left: 42px; width: 182px; height: 182px; border-radius: 50%; background: var(--plan-blue); border: 15px solid var(--white); }
  .plan-1 { top: 1049px; } .marker-1 { top: 1124px; }
  .plan-2 { top: 1486px; } .marker-2 { top: 1552px; }
  .plan-3 { top: 1921px; } .marker-3 { top: 1990px; }

  .network-art { position: absolute; left: 0; top: 2320px; width: 1200px; height: 719px; }

  .availability { position: absolute; left: 50px; top: 2520px; width: 1100px; text-align: center; color: var(--white); font-size: 56px; font-weight: 600; line-height: 1.35; }

  .contact { position: absolute; left: 0; width: 1200px; height: 144px; display: flex; color: var(--white); }
  .contact-label { width: 233px; display: flex; align-items: center; justify-content: center; font-size: 64px; font-weight: 600; }
  .contact-value { flex: 1; display: flex; align-items: center; padding-left: 70px; font-size: 66px; }
  .contact-web { top: 3039px; } .contact-web .contact-label { background: var(--ink); } .contact-web .contact-value { background: var(--plan-blue); }
  .contact-phone { top: 3183px; } .contact-phone .contact-label { background: var(--plan-blue); } .contact-phone .contact-value { background: var(--ink); }
</style>
</head>
<body>
<main class="hanger">
  <header class="masthead">
    <span class="punch-hole" aria-hidden="true"></span>
    <div class="brand">
      <span class="brand-dot"></span>
      <span class="brand-name">Brivanet</span>
    </div>
    <div class="brand-tagline">Internet Services</div>
  </header>

  <div class="title-band"><h1>Brivanet Internet Services</h1></div>

  <div class="backdrop" role="img" aria-label="Soft grey photo of leaves behind the plan list"></div>

  <section class="plans">
    <div class="plan plan-1"><p>100 Mbps $XX.XX<br>per month</p></div>
    <span class="plan-marker marker-1"></span>
    <div class="plan plan-2"><p>250 Mbps $XX.XX<br>per month</p></div>
    <span class="plan-marker marker-2"></span>
    <div class="plan plan-3"><p>1 Gbps $XX.XX<br>per month</p></div>
    <span class="plan-marker marker-3"></span>
  </section>

  <svg class="network-art" viewBox="0 0 1200 719" role="img" aria-label="Illustration of hands holding a glowing globe linked to connected devices">
    <defs>
      <linearGradient id="network-fill" x1="0" y1="0" x2="0" y2="1">
        <stop offset="0" stop-color="#2f6c96"/>
        <stop offset="1" stop-color="#0c2236"/>
      </linearGradient>
    </defs>
    <polygon points="0,120 600,10 1200,120 1200,719 0,719" fill="url(#network-fill)"/>
    <polyline points="0,120 600,10 1200,120" fill="none" stroke="#8fc5ec" stroke-width="10"/>
  </svg>

  <p class="availability">Glass Bolt Internet Service<br>is Now Available in Cedar Hollow!</p>

  <div class="contact contact-web">
    <div class="contact-label">W</div>
    <div class="contact-value">www.brivanet.example</div>
  </div>
  <div class="contact contact-phone">
    <div class="contact-label">T</div>
    <div class="contact-value">555-304-2968</div>
  </div>
</main>
</body>
</html>
```